Etiketten für Vodka
Zielgruppe
Herstellung und Abfüllung von Spirituosen
Zielgruppe für die Kubus Range sind Bars, Clubs, Feste/Festivals
Aufgabenstellung
Unsere Kubus-Range umfasst rund 40 Spirituosen und deckt nahezu alles ab, was in einer modernen und gut sortierten Theke nicht fehlen darf.
Zum Jahreswechsel möchten wir die gesamte Range relaunchen und suchen im ersten Schritt ein Vorder-, Rückenetikett und Halsschleife für den Hauptartikel Vodka, welches in nachfolgenden Schritten auf die anderen Artikel übertragen werden soll.
Das Design soll wertig sein, auf unsere eigene Herstellung von Destillaten und Kräuterauszügen hinweisen.
Bei dem bestehenden Design kann der Barkeeper die Sorten leicht unterscheiden, dies soll auch weiterhin so bleiben.
Das Logo 'Kubus' ist eine eingetragen Wort-Bild-Marke und muss im Vorderetikett bestehen bleiben.
Max Größe Vorderetikett: Höhe 150mm, Breite 60mm
Max Größe Rückenetikett: Höhe 100mm, Breite 40mm

```html
<!DOCTYPE html>
<html lang="de">
<head>
<meta charset="utf-8">
<title>Kubus Pure Vodka – Etiketten</title>
<link href="https://fonts.googleapis.com/css2?family=Barlow:wght@500;600;700&family=Barlow+Semi+Condensed:wght@600;700&display=swap" rel="stylesheet">
<style>
  :root {
    --navy: #2b2170;
    --navy-deep: #211a5c;
    --sky: #2fa3e6;
    --ice: #8fd3ff;
    --photo-dark: #0b3f8f;
    --photo-mid: #1a7fd0;
    --photo-light: #7cc8f5;
    --rule: #c9ccd4;
    --white: #ffffff;
    --black: #0a0a0a;
    --page: #eef0f3;
  }
  * { box-sizing: border-box; margin: 0; padding: 0; }
  html, body { width: 1200px; height: 2199px; overflow: hidden; background: var(--page); }
  body { position: relative; font-family: "Barlow", "Arial", sans-serif; }

  /* Neck band */
  .neck-band {
    position: absolute; left: 760px; top: 150px; width: 360px; height: 210px;
    background: var(--navy); display: flex; flex-direction: column;
    align-items: center; justify-content: center;
    border-top: 8px solid var(--rule); border-bottom: 8px solid var(--rule);
  }
  .neck-band .variant { color: var(--sky); font-weight: 600; font-size: 30px; letter-spacing: 1px; }
  .neck-band .product { color: var(--white); font-weight: 700; font-size: 74px; line-height: 1; letter-spacing: 1px; }

  /* Shared label pieces */
  .label { position: absolute; background: var(--white); display: flex; flex-direction: column; overflow: hidden; box-shadow: 0 6px 24px rgba(20,20,60,.15); }
  .label-header {
    position: relative; display: flex; align-items: center; justify-content: center;
    background: radial-gradient(circle at 20% 30%, var(--photo-light) 0, transparent 35%),
                radial-gradient(circle at 85% 60%, var(--photo-light) 0, transparent 30%),
                linear-gradient(135deg, var(--photo-mid), var(--photo-dark));
  }
  .brand-plate {
    background: var(--black); border-radius: 12px; display: flex; align-items: center; justify-content: center;
  }
  .brand-name { color: var(--white); font-weight: 600; letter-spacing: 6px; }
  .title-band { background: var(--navy); display: flex; flex-direction: column; align-items: center; justify-content: center; }
  .title-band .variant { color: var(--sky); font-weight: 600; }
  .title-band .product { color: var(--white); font-weight: 700; line-height: 1; letter-spacing: 2px; text-shadow: 0 2px 0 var(--ice); }
  .rule { background: var(--rule); }
  .footer-bar { background: var(--navy); color: var(--white); font-weight: 600; display: flex; align-items: center; }

  /* Front label */
  .front-label { left: 80px; top: 150px; width: 620px; height: 1540px; }
  .front-label .label-header { height: 230px; }
  .front-label .brand-plate { width: 440px; height: 120px; }
  .front-label .brand-name { font-size: 84px; }
  .front-label .title-band { height: 310px; }
  .front-label .variant { font-size: 50px; margin-bottom: 6px; }
  .front-label .product { font-size: 150px; }
  .front-label .rule { height: 12px; }
  .pour-photo {
    flex: 1;
    background: radial-gradient(ellipse at 50% 75%, var(--photo-light) 0, transparent 45%),
                linear-gradient(180deg, var(--photo-mid) 0%, var(--photo-dark) 55%, var(--photo-mid) 100%);
  }
  .front-label .footer-bar { height: 82px; justify-content: space-between; padding: 0 36px; font-size: 36px; }

  /* Back label */
  .back-label { left: 760px; top: 470px; width: 360px; height: 890px; }
  .back-label .label-header { height: 130px; }
  .back-label .brand-plate { width: 280px; height: 74px; border-radius: 8px; }
  .back-label .brand-name { font-size: 52px; letter-spacing: 4px; }
  .back-label .title-band { height: 180px; }
  .back-label .variant { font-size: 32px; margin-bottom: 2px; }
  .back-label .product { font-size: 86px; }
  .back-label .rule { height: 8px; }
  .back-copy {
    flex: 1; text-align: center; font-family: "Barlow Semi Condensed", "Arial Narrow", sans-serif;
    font-weight: 700; font-size: 23px; line-height: 1.35; padding-top: 52px;
  }
  .back-copy .heading { color: var(--navy); font-size: 25px; margin-bottom: 22px; }
  .back-copy .claim { color: var(--sky); margin-bottom: 52px; }
  .back-copy .producer { color: var(--navy); margin-bottom: 18px; }
  .back-copy .origin { color: var(--navy); }
  .back-label .footer-bar { height: 50px; justify-content: center; font-size: 25px; letter-spacing: .5px; font-family: "Barlow Semi Condensed", "Arial Narrow", sans-serif; }
</style>
</head>
<body>

  <div class="neck-band">
    <span class="variant">PURE</span>
    <span class="product">VODKA</span>
  </div>

  <section class="label front-label">
    <div class="label-header" role="img" aria-label="Unscharfer blauer Bar-Lichter-Hintergrund">
      <div class="brand-plate"><span class="brand-name">KUBUS</span></div>
    </div>
    <div class="title-band">
      <span class="variant">PURE</span>
      <span class="product">VODKA</span>
    </div>
    <div class="rule"></div>
    <div class="pour-photo" role="img" aria-label="Foto: Vodka wird aus einem Ausgießer in ein Shotglas auf Eis gegossen, in Blau getönt"></div>
    <div class="footer-bar"><span>37,5% Vol.</span><span>1 Liter</span></div>
  </section>

  <section class="label back-label">
    <div class="label-header" role="img" aria-label="Unscharfer blauer Bar-Lichter-Hintergrund">
      <div class="brand-plate"><span class="brand-name">KUBUS</span></div>
    </div>
    <div class="title-band">
      <span class="variant">PURE</span>
      <span class="product">VODKA</span>
    </div>
    <div class="rule"></div>
    <div class="back-copy">
      <p class="heading">ÜBERSCHRIFT</p>
      <p class="claim">Hier ein Text zum<br>hochwertigen Produkt<br>aus eigener Herstellung.<br>Spaß Kubus Text<br>und weitere<br>Angaben.</p>
      <p class="producer">Hersteller:<br>HANNO VELDRIK e.K.<br>Lindenhofweg 7<br>54321 Burgtal</p>
      <p class="origin">Ursprung: Deutschland</p>
    </div>
    <div class="footer-bar">HOTLINE: 01234/5678901</div>
  </section>

</body>
</html>
```